Business Card Design for Cybersecurity Company - Quorvent Systems

We need a business card design for our new cybersecurity company, Quorvent. We’re going for a clean, hi tech look that feels modern, premium, and trustworthy. We want a design that really stands out and makes people say WOW when we hand it over!

Quorvent delivers reliable IT support and managed services for small and mid sized businesses. We help companies stay secure, efficient, and connected through proactive monitoring, cybersecurity services, cloud management, and remote support.

Target Market(s)

Designers should target small and mid sized businesses that need dependable cybersecurity and IT support.

Industry/Entity Type

Cybersecurity, Managed Service Provider, IT services

Contact Information for Business Card

Contact information

Requirements
Must have
• The card should look clean, modern, and tech focused, with the Quorvent logo, clear contact info, and strong readability. It needs to feel premium and professional while still keeping a simple layout that fits a cybersecurity and IT brand.
Nice to have
• Nice to have elements include subtle touches that give the card a modern, tech feel, along with a layout that works well in different background styles.
Should not have
• The card should avoid clutter, loud graphics, or anything that takes attention away from the logo and contact details.

```html
<!DOCTYPE html>
<html lang="en">
<head>
<meta charset="utf-8">
<title>Quorvent Systems – Business Card</title>
<link rel="stylesheet" href="https://fonts.googleapis.com/css2?family=Poppins:wght@400;500;600;700&display=swap">
<style>
  :root {
    --page-bg: #2b2b2e;
    --card-bg: #ffffff;
    --brand-blue: #3f6fc4;
    --brand-violet: #5b3fa6;
    --brand-mark: #4a52b4;
    --ink: #1f1f24;
    --swoosh-dark: #333336;
    --on-brand: #ffffff;
  }
  * { box-sizing: border-box; margin: 0; padding: 0; }
  html, body { width: 1200px; height: 880px; overflow: hidden; }
  body {
    background: var(--page-bg);
    font-family: "Poppins", sans-serif;
    display: flex;
    flex-direction: column;
    align-items: center;
    justify-content: center;
    gap: 48px;
  }
  .card {
    position: relative;
    width: 630px;
    height: 360px;
    background: var(--card-bg);
    border-radius: 22px;
    overflow: hidden;
  }

  /* Brand name lockup */
  .brand {
    display: flex;
    align-items: center;
    gap: 12px;
    color: var(--brand-mark);
    font-weight: 600;
    white-space: nowrap;
  }
  .brand-dot {
    width: 20px; height: 20px;
    border-radius: 50%;
    background: var(--brand-mark);
    flex: none;
  }

  /* Back side */
  .card-back {
    display: flex;
    flex-direction: column;
    align-items: center;
    justify-content: center;
    text-align: center;
  }
  .card-back .brand { font-size: 46px; margin-bottom: 34px; }
  .services-title {
    color: var(--brand-blue);
    font-weight: 700;
    font-size: 20px;
    letter-spacing: 0.5px;
    margin-bottom: 6px;
  }
  .services-list {
    color: var(--ink);
    font-size: 15px;
    font-weight: 500;
  }

  /* Front side */
  .card-front .wave {
    position: absolute;
    inset: 0;
    width: 100%;
    height: 100%;
  }
  .card-front .brand {
    position: absolute;
    left: 40px;
    top: 62px;
    font-size: 32px;
  }
  .person {
    position: absolute;
    left: 44px;
    top: 178px;
  }
  .person-name {
    color: var(--brand-violet);
    font-weight: 700;
    font-size: 24px;
    letter-spacing: 0.4px;
  }
  .person-role {
    color: var(--ink);
    font-size: 14px;
    font-weight: 500;
  }
  .contact {
    position: absolute;
    right: 28px;
    top: 160px;
    list-style: none;
    color: var(--on-brand);
    font-size: 15px;
    line-height: 1.55;
    text-align: right;
  }
  .contact li {
    display: flex;
    align-items: center;
    justify-content: flex-end;
    gap: 8px;
  }
  .contact svg { width: 13px; height: 13px; flex: none; }
</style>
</head>
<body>

  <section class="card card-back" aria-label="Business card, back">
    <div class="brand"><span class="brand-dot"></span><span>Quorvent Systems</span></div>
    <h2 class="services-title">OUR SERVICES</h2>
    <p class="services-list">Cybersecurity | Cloud Solutions | Network Management | IT Consulting</p>
  </section>

  <section class="card card-front" aria-label="Business card, front">
    <svg class="wave" viewBox="0 0 630 360" preserveAspectRatio="none" aria-hidden="true">
      <defs>
        <linearGradient id="brandGradient" x1="0" y1="0" x2="0.3" y2="1">
          <stop offset="0" stop-color="#4a7cc6"/>
          <stop offset="1" stop-color="#5f3fa3"/>
        </linearGradient>
      </defs>
      <path d="M50 346 C210 330 320 290 375 180 C395 135 410 100 432 82 C402 122 382 162 362 205 C320 292 220 330 70 340 Z" fill="var(--swoosh-dark)"/>
      <path d="M560 0 L630 0 L630 360 L90 360 C240 345 340 300 400 190 C440 110 480 40 560 0 Z" fill="url(#brandGradient)"/>
      <path d="M130 352 C270 332 352 290 406 190 C446 106 492 44 592 8" fill="none" stroke="#ffffff" stroke-width="5"/>
    </svg>

    <div class="brand"><span class="brand-dot"></span><span>Quorvent Systems</span></div>

    <div class="person">
      <h1 class="person-name">DANA WHITFIELD</h1>
      <p class="person-role">Owner | CEO | Quorvent Systems</p>
    </div>

    <ul class="contact">
      <li>(855) 410-7720
        <svg viewBox="0 0 16 16"><path fill="currentColor" d="M3 1h3l1.5 4-2 1.2a9 9 0 0 0 4.3 4.3L11 8.5l4 1.5v3a2 2 0 0 1-2 2A12 12 0 0 1 1 3a2 2 0 0 1 2-2z"/></svg>
      </li>
      <li>(813) 555-0187
        <svg viewBox="0 0 16 16"><rect x="4" y="1" width="8" height="14" rx="1.5" fill="none" stroke="currentColor" stroke-width="1.6"/></svg>
      </li>
      <li>dana@quorvent.com
        <svg viewBox="0 0 16 16"><rect x="1" y="3" width="14" height="10" fill="currentColor"/><path d="M1 3l7 6 7-6" fill="none" stroke="#5f4aa8" stroke-width="1.3"/></svg>
      </li>
      <li>quorvent.com
        <svg viewBox="0 0 16 16"><g fill="none" stroke="currentColor" stroke-width="1.3"><circle cx="8" cy="8" r="6.5"/><ellipse cx="8" cy="8" rx="3" ry="6.5"/><path d="M1.5 8h13"/></g></svg>
      </li>
    </ul>
  </section>

</body>
</html>
```